ROLLER SKATING RINK 5" Round Flyer

We are a skating rink in Miami Fl. This flyer will be used as our Fall Schedule. I have drawn up a sketch of what we are looking to do. We will work out wording and font styles later. I have all the copy needed for the flyer. I am open to your thoughts on the design if you have any to offer.

Target Market(s)

Kids from 8 years old to Adults.

Colors

Designer to choose colors to be used in the design.

Requirements
Must have
• Our company logo placed in the middle. I have this file and will send to anyone who needs it.
• READABILITY - CREATIVITY - FUN
Nice to have
• Colors that make you think MIAMI.
Should not have
• keep it PG, please. =)

```html
<!DOCTYPE html>
<html lang="en">
<head>
<meta charset="utf-8">
<title>Rollway Skating Center – Fall Schedule</title>
<link rel="stylesheet" href="https://fonts.googleapis.com/css2?family=Bungee+Inline&family=Josefin+Sans:wght@300;400;600;700&family=Limelight&display=swap">
<style>
  :root {
    --rink-green: #4f7d6e;
    --sunny-yellow: #f8de72;
    --flamingo-pink: #f2c4c0;
    --mint: #b6f1d3;
    --divider-red: #d98a86;
    --paper: #ffffff;
  }
  html, body {
    margin: 0;
    padding: 0;
    width: 1181px;
    height: 1200px;
    overflow: hidden;
    background: var(--paper);
  }
  .schedule-wheel {
    display: block;
    width: 1181px;
    height: 1200px;
  }
  .ring-frame { fill: none; stroke: var(--rink-green); }
  .divider { stroke: var(--rink-green); stroke-width: 1.2; }
  .divider--red { stroke: var(--divider-red); }
  .session-arc { fill: none; stroke: var(--rink-green); stroke-width: 5; }
  .day-name {
    font-family: "Limelight", serif;
    font-size: 60px;
    letter-spacing: 4px;
    fill: var(--flamingo-pink);
  }
  .event-title {
    font-family: "Bungee Inline", sans-serif;
    font-size: 62px;
    fill: var(--sunny-yellow);
    text-anchor: middle;
  }
  .event-title--large { font-size: 72px; }
  .free-tag {
    font-family: "Bungee Inline", sans-serif;
    font-size: 52px;
    fill: var(--mint);
    stroke: var(--sunny-yellow);
    stroke-width: 1.5;
    text-anchor: middle;
  }
  .free-tag--small { font-size: 44px; }
  .closed-label {
    font-family: "Josefin Sans", sans-serif;
    font-weight: 300;
    font-size: 80px;
    fill: var(--flamingo-pink);
    stroke: var(--flamingo-pink);
    stroke-width: 1.5;
    text-anchor: middle;
  }
  .lesson-label {
    font-family: "Josefin Sans", sans-serif;
    font-weight: 600;
    font-size: 60px;
    fill: var(--paper);
    stroke: var(--rink-green);
    stroke-width: 2.5;
    text-anchor: middle;
  }
  .party-label {
    font-family: "Josefin Sans", sans-serif;
    font-weight: 700;
    font-size: 44px;
    fill: var(--paper);
    stroke: var(--rink-green);
    stroke-width: 2.4;
    text-anchor: middle;
  }
  .party-tagline {
    font-family: "Josefin Sans", sans-serif;
    font-weight: 400;
    font-size: 22px;
    fill: var(--rink-green);
    text-anchor: middle;
    text-decoration: underline;
  }
  .time-label {
    font-family: "Josefin Sans", sans-serif;
    font-weight: 400;
    font-size: 17px;
    fill: var(--rink-green);
  }
  .hub { fill: var(--rink-green); }
  .rink-name {
    font-family: "Josefin Sans", sans-serif;
    font-weight: 700;
    fill: #fbf3cf;
    text-anchor: middle;
  }
</style>
</head>
<body>
<svg class="schedule-wheel" viewBox="0 0 1345 1366" xmlns="http://www.w3.org/2000/svg" aria-labelledby="wheel-title">
  <title id="wheel-title">Rollway Skating Center weekly schedule wheel</title>
  <defs>
    <path id="upper-day-track" d="M118 693 A555 555 0 0 1 1228 693"/>
    <path id="lower-day-track" d="M71 693 A602 602 0 0 0 1275 693"/>
  </defs>

  <g class="dividers">
    <line class="divider divider--red" x1="673" y1="63" x2="673" y2="1323"/>
    <line class="divider" x1="43" y1="693" x2="1303" y2="693"/>
    <line class="divider" x1="513" y1="533" x2="228" y2="248"/>
    <line class="divider" x1="833" y1="853" x2="1118" y2="1138"/>
    <line class="divider" x1="513" y1="853" x2="228" y2="1138"/>
  </g>

  <circle class="ring-frame" cx="673" cy="693" r="630" stroke-width="8"/>
  <circle class="ring-frame" cx="673" cy="693" r="527" stroke-width="11"/>

  <path class="session-arc" d="M427 447 A348 348 0 0 1 673 345"/>
  <path class="session-arc" d="M919 447 A348 348 0 0 1 1021 693"/>
  <path class="session-arc" d="M919 939 A348 348 0 0 1 325 693"/>

  <g class="day-arrow">
    <line x1="833" y1="533" x2="1095" y2="271" stroke="var(--rink-green)" stroke-width="5"/>
    <polygon points="1110,256 1072,268 1098,294" fill="var(--rink-green)"/>
    <text class="time-label" transform="translate(842 528) rotate(-45)">MORNING</text>
    <text class="time-label" transform="translate(980 390) rotate(-45)">EVENING</text>
  </g>

  <g class="day-names">
    <text class="day-name" text-anchor="middle"><textPath href="#upper-day-track" startOffset="12.5%">BIRTHDAY</textPath></text>
    <text class="day-name" text-anchor="middle"><textPath href="#upper-day-track" startOffset="37.5%">MONDAY</textPath></text>
    <text class="day-name" text-anchor="middle"><textPath href="#upper-day-track" startOffset="62.5%">TUESDAY</textPath></text>
    <text class="day-name" text-anchor="middle"><textPath href="#upper-day-track" startOffset="87.5%">WEDNESDAY</textPath></text>
    <text class="day-name" text-anchor="middle"><textPath href="#lower-day-track" startOffset="12.5%">SUNDAY</textPath></text>
    <text class="day-name" text-anchor="middle"><textPath href="#lower-day-track" startOffset="37.5%">SATURDAY</textPath></text>
    <text class="day-name" text-anchor="middle"><textPath href="#lower-day-track" startOffset="62.5%">FRIDAY</textPath></text>
    <text class="day-name" text-anchor="middle"><textPath href="#lower-day-track" startOffset="87.5%">THURSDAY</textPath></text>
  </g>

  <!-- Monday -->
  <text class="event-title event-title--large" transform="translate(500 287) rotate(-18)" textLength="195" lengthAdjust="spacingAndGlyphs">ADULT</text>
  <text class="event-title event-title--large" transform="translate(523 358) rotate(-18)" textLength="210" lengthAdjust="spacingAndGlyphs">NIGHT</text>
  <text class="free-tag" transform="translate(564 433) rotate(-18)" textLength="120" lengthAdjust="spacingAndGlyphs">FREE</text>

  <!-- Tuesday -->
  <text class="closed-label" transform="translate(812 361) rotate(20)" textLength="262" lengthAdjust="spacingAndGlyphs">CLOSED</text>

  <!-- Wednesday -->
  <text class="lesson-label" transform="translate(1098 547) rotate(70)" textLength="215" lengthAdjust="spacingAndGlyphs">SKATE</text>
  <text class="lesson-label" transform="translate(1028 537) rotate(70)" textLength="255" lengthAdjust="spacingAndGlyphs">LESSONS</text>
  <text class="free-tag" transform="translate(926 586) rotate(70)" textLength="130" lengthAdjust="spacingAndGlyphs">FREE</text>

  <!-- Friday -->
  <text class="free-tag free-tag--small" transform="translate(778 955) rotate(-20)" textLength="135" lengthAdjust="spacingAndGlyphs">CHEAP</text>
  <text class="free-tag free-tag--small" transform="translate(802 1010) rotate(-20)" textLength="125" lengthAdjust="spacingAndGlyphs">SKATE</text>
  <text class="event-title" transform="translate(822 1071) rotate(-20)" textLength="195" lengthAdjust="spacingAndGlyphs">FRIDAY</text>
  <text class="event-title" transform="translate(864 1156) rotate(-20)" textLength="175" lengthAdjust="spacingAndGlyphs">NIGHT</text>

  <!-- Saturday -->
  <text class="free-tag" transform="translate(554 973) rotate(20)" textLength="125" lengthAdjust="spacingAndGlyphs">FREE</text>
  <text class="event-title" transform="translate(505 1091) rotate(20)" textLength="285" lengthAdjust="spacingAndGlyphs">SATURDAY</text>
  <text class="event-title" transform="translate(483 1161) rotate(20)" textLength="185" lengthAdjust="spacingAndGlyphs">NIGHT</text>

  <!-- Sunday -->
  <text class="free-tag" transform="translate(400 812) rotate(70)" textLength="130" lengthAdjust="spacingAndGlyphs">FREE</text>
  <text class="event-title" transform="translate(284 847) rotate(70)" textLength="225" lengthAdjust="spacingAndGlyphs">FAMILY</text>
  <text class="event-title" transform="translate(224 877) rotate(70)" textLength="205" lengthAdjust="spacingAndGlyphs">NIGHT</text>

  <!-- Birthday -->
  <g transform="translate(300 545) rotate(-62)">
    <text class="party-label" y="-48" textLength="320" lengthAdjust="spacingAndGlyphs">BOOK&#160;&#160;&#160;&#160;YOUR</text>
    <text class="party-label" y="6" textLength="300" lengthAdjust="spacingAndGlyphs">NEXT PARTY</text>
    <text class="party-label" y="60" x="40" textLength="165" lengthAdjust="spacingAndGlyphs">HERE !</text>
  </g>
  <g transform="translate(422 590) rotate(-62)">
    <text class="party-tagline" y="-8">PARTY ON</text>
    <text class="party-tagline" y="22">WHEELS</text>
  </g>

  <g class="hub-group">
    <circle class="hub" cx="673" cy="693" r="226"/>
    <text class="rink-name" x="673" y="690" font-size="64">ROLLWAY</text>
    <text class="rink-name" x="673" y="740" font-size="28" letter-spacing="3">SKATING CENTER</text>
  </g>
</svg>
</body>
</html>
```